Buch-/eBook-Cover Thema Wohnungssuche
Zielgruppe
Das Buch ist für alle, die auf der Suche nach einer Mietwohnung/Haus sind. Es gibt Tipps, wie man die Chancen auf eine Zusage bekommt.
Aufgabenstellung
Das Buch wird von Katrin Elise Bode von der Firma Lindenkamm geschrieben. Die Firma Lindenkamm ist aber nicht im Fokus, es muss auch nicht das CI der Firma sein. Wichtig ist, dass sie aber auf dem Buch ist.
Haupttitel: Wie finde ich eine passende Mietwohnung?
Untertitel: Insiderwissen vom Vermieter – so überzeugst du Vermieter und bekommst endlich die Zusage für deine Traumwohnung.
Rückseitentext:
Ständig Absagen bei der Wohnungssuche oder überhaupt keine Rückmeldungen? Dieses Buch zeigt dir aus erster Hand, worauf Vermieter wirklich achten – vom überzeugenden Anschreiben über den Besichtigungstermin bis zum Mietvertrag, samt Kaution, Nebenkosten, Jobcenter, Checklisten, Glossar und was es sonst noch alles zu beachten gibt.
Echtes Praxiswissen aus über zehn Jahren als Vermieterin und Immobilienmaklerin – keine KI-Texte, sondern ehrliche Erfahrung aus dem realen Wohnungsmarkt. Katrin Elise Bode erklärt dir alles verständlich und sofort umsetzbar.
So machst du aus „leider nicht' ein „Herzlich Willkommen in deinem neuen Zuhause'.
Format: A5, Hardcover mit rundem Rand.
Frau Bode soll auf dem Titel zu sehen sein.
Das Design darf nicht zu überladen sein.

```html
<!DOCTYPE html>
<html lang="de">
<head>
<meta charset="utf-8">
<title>Wie finde ich eine passende Mietwohnung? – Buchumschlag</title>
<link rel="stylesheet" href="https://fonts.googleapis.com/css2?family=Lato:wght@400;700&family=Montserrat:wght@700;800&display=swap">
<style>
  :root {
    --page-bg: #d9d9d9;
    --back-cream: #fbf9e8;
    --olive: #6e7d4f;
    --olive-text: #556b35;
    --forest: #234d2e;
    --ink: #1e1e1e;
    --white: #ffffff;
    --badge-green: #7bd55a;
    --badge-ring: #2f5a22;
  }
  * { box-sizing: border-box; margin: 0; padding: 0; }
  html, body { width: 960px; height: 1200px; overflow: hidden; }
  body {
    background: var(--page-bg);
    position: relative;
    font-family: "Lato", sans-serif;
  }
  .cover {
    position: absolute;
    left: 30px; top: 283px;
    width: 900px; height: 634px;
    display: flex;
    box-shadow: 0 12px 40px rgba(0,0,0,.18);
  }
  /* Back */
  .back {
    position: relative;
    width: 411px; height: 100%;
    background: var(--back-cream);
    overflow: hidden;
  }
  .back-heading {
    position: absolute; left: 54px; top: 37px;
    font-family: "Montserrat", sans-serif; font-weight: 700;
    font-size: 20px; color: var(--olive-text);
  }
  .back-copy {
    position: absolute; left: 54px; top: 91px; width: 330px;
    font-size: 14px; line-height: 23.3px; color: var(--ink);
  }
  .back-copy p + p { margin-top: 23px; }
  .back-band {
    position: absolute; left: 0; bottom: 0;
    width: 100%; height: 42px; background: var(--olive);
  }
  .back-portrait {
    position: absolute; left: 70px; top: 477px;
    width: 145px; height: 157px;
    background: linear-gradient(180deg, #c9b9a6 0%, #e8e2d8 45%, #4f6b3a 75%, #3f5a2e 100%);
    border-radius: 60px 60px 0 0;
  }
  .back-author {
    position: absolute; right: 43px; bottom: 16px;
    font-size: 11.5px; color: var(--white);
  }
  /* Spine */
  .spine {
    width: 77px; height: 100%;
    display: flex; flex-direction: column;
  }
  .spine-top {
    height: 181px; background: var(--olive);
    display: flex; justify-content: center; padding-top: 20px;
  }
  .spine-bottom {
    flex: 1; background: var(--forest);
    display: flex; justify-content: center; padding-top: 30px;
  }
  .spine-author {
    writing-mode: vertical-rl;
    font-size: 14px; color: var(--white);
  }
  .spine-title {
    writing-mode: vertical-rl;
    font-family: "Montserrat", sans-serif; font-weight: 700;
    font-size: 17px; color: var(--white);
  }
  /* Front */
  .front {
    position: relative;
    width: 412px; height: 100%;
    overflow: hidden;
  }
  .front-photo {
    position: absolute; inset: 0;
    background:
      radial-gradient(ellipse at 72% 60%, rgba(220,215,200,.35) 0%, rgba(0,0,0,0) 45%),
      linear-gradient(180deg, #7f9a55 0%, #5f7f48 30%, #3f5f35 65%, #2f4a2a 100%);
  }
  .front-title {
    position: absolute; left: 0; right: 0; top: 32px;
    text-align: center;
    font-family: "Montserrat", sans-serif; font-weight: 800;
    font-size: 45px; line-height: 51px; color: var(--white);
    letter-spacing: 0.5px;
    text-shadow: 0 2px 6px rgba(0,0,0,.25);
  }
  .front-subtitle {
    position: absolute; left: 37px; top: 193px;
    font-size: 16px; color: #f2f2ea;
  }
  .front-badge {
    position: absolute; left: 37px; top: 425px;
    width: 112px; height: 112px;
  }
  .front-author {
    position: absolute; left: 37px; top: 573px;
    font-size: 15px; color: var(--white);
  }
</style>
</head>
<body>
  <div class="cover">
    <section class="back">
      <h2 class="back-heading">Rückseitentext</h2>
      <div class="back-copy">
        <p>Ständig Absagen bei der Wohnungssuche oder<br>überhaupt keine Rückmeldungen? Dieses Buch zeigt<br>dir aus erster Hand, worauf Vermieter wirklich<br>achten – vom überzeugenden Anschreiben über den<br>Besichtigungstermin bis zum Mietvertrag, samt<br>Kaution, Nebenkosten, Jobcenter, Checklisten,<br>Glossar und was es sonst noch alles zu beachten gibt.</p>
        <p>Echtes Praxiswissen aus über zehn Jahren als<br>Vermieterin und Immobilienmaklerin – keine KI-<br>Texte, sondern ehrliche Erfahrung aus dem realen<br>Wohnungsmarkt. Katrin Elise Bode erklärt dir<br>alles verständlich und sofort umsetzbar.</p>
        <p>So machst du aus „leider nicht' ein „Herzlich<br>Willkommen in deinem neuen Zuhause'.</p>
      </div>
      <div class="back-band"></div>
      <div class="back-portrait" role="img" aria-label="Porträtfoto der Autorin im grünen Dirndl"></div>
      <span class="back-author">Katrin Elise Bode</span>
    </section>

    <section class="spine">
      <div class="spine-top"><span class="spine-author">Katrin Elise Bode</span></div>
      <div class="spine-bottom"><span class="spine-title">Wie finde ich eine passende Mietwohnung?</span></div>
    </section>

    <section class="front">
      <div class="front-photo" role="img" aria-label="Foto der lächelnden Autorin im grünen Dirndl vor einem sonnigen Wald"></div>
      <h1 class="front-title">Wie finde ich<br>eine passende<br>Mietwohnung?</h1>
      <p class="front-subtitle">Insiderwissen vom Vermieter</p>
      <svg class="front-badge" viewBox="0 0 112 112" aria-label="Sofort umsetzbare Praxis-Tipps">
        <circle cx="56" cy="56" r="55" fill="var(--badge-green)"/>
        <circle cx="56" cy="56" r="45" fill="none" stroke="var(--badge-ring)" stroke-width="1.2"/>
        <g transform="rotate(-14 56 56)" font-family="Lato, sans-serif" font-size="12" fill="#1f2a18" text-anchor="middle">
          <text x="56" y="44">Sofort</text>
          <text x="56" y="60">umsetzbare</text>
          <text x="56" y="76">Praxis-Tipps</text>
        </g>
      </svg>
      <p class="front-author">Katrin Elise Bode</p>
    </section>
  </div>
</body>
</html>
```